TRNV LLP website - revamping our website after 23 years

Our website needs a complete overhaul. The purpose of this exercise is to provide us with your vision of what you think the website should look like. We don't need the website to be created or coded. Just need creative designs.

We have a four sites that we would like to base our website on;

We like the simplicity of Fairwicks, the style of Pemberly Strand and Kettridge.

http://www.pemberlystrand-example.com/en/toronto-ontario/
http://www.fairwicks-example.ca/
hallkettridge-example.com
http://www.vendrupe-example.com/our-professionals.html

We have a logo that we would like to use which will be attached below. We need to keep our website looking very professional as we have a large number of high net worth clients.
Updates

Hi, We've received some good website designs but they appear to be the same type of template websites we've received in the past - this is not what we're looking for. What we want is a unique website that is modelled on the following three company websites: http://www.fairwicks-example.ca/ www.hallkettridge-example.com/ http://www.pemberlystrand-example.com/en/toronto-ontario/

Thank you everyone for your designs. I will be posting updates and my comments on the various designs in the next day - I want to thank you for the creative designs I see. I thought i would explain a bit about our firm and perhaps it can help when you design the theme of our website: - Our firm is like a family and our clients are truly like our friends. We have close knit relationships in and outside of the office with staff and clients. - We are an 'out of the box' type of firm. We operate differently than most firms and that's a differentiating factor in what makes us who we are - Our slogan is "Count on us" which is a testament to the way we run our practice - We would like an open, fresh, clean look to our website - we don't want the landing page to be overly long or complex because we have limited time to update the website and limited content That's it for the time being - when things come to mind I will post them here.

Can we try a design as follows: - make the website look very similar to www.fairwicks-example.ca - use the same background colour - Keep the same black top but insert our logo - incorporate some of the content from our current website www.trnv-example.com

I have been away dealing with a personal matter. I will look into these websites tomorrow afternoon and provide more feedback / info on the top designer. Thank you

Hi designers, I want to apologize for the delay. I plan on wrapping things up within the next few days. I will go through a few of the top designs and offer my comments. Thank you for your patience.

Target Market(s)

Mainly our current clients - We have a large number of high net worth individuals as clients.

Industry/Entity Type

Accounting

Number of Pages Required

1 page

Requirements
Must have
• Please model website on the websites indicated above.
• Our current website is www.trnv-example.com. It's dark, cluttered and not inviting. We want a fresh, clean website. Please incorporate the logo's attached below.

```html
<!DOCTYPE html>
<html lang="en">
<head>
<meta charset="utf-8">
<title>TRNV LLP — Chartered Professional Accountants</title>
<link href="https://fonts.googleapis.com/css2?family=Open+Sans:wght@300;400;600;700&display=swap" rel="stylesheet">
<style>
:root{
  --header-bg:#23262a;
  --footer-bg:#2a2d31;
  --accent:#29b6e3;
  --accent-panel:rgba(38,168,210,0.86);
  --text-muted:#9a9a9a;
  --text-dark:#2b2b2b;
  --white:#ffffff;
  --rule:#4a4e54;
  --teal-deep:#0e4358;
  --teal-mid:#1a5f78;
}
*{margin:0;padding:0;box-sizing:border-box}
html,body{width:1053px;height:1200px;overflow:hidden;background:var(--white)}
body{position:relative;font-family:'Open Sans',Arial,sans-serif;color:var(--text-muted)}

.site-header{position:absolute;left:0;top:0;width:1053px;height:73px;background:var(--header-bg)}
.brand{position:absolute;left:204px;top:36px;display:flex;align-items:center;gap:6px;color:var(--white);font-size:16px;font-weight:400;letter-spacing:.3px}
.brand-mark{width:11px;height:11px;background:var(--accent)}
.brand-sub{position:absolute;left:205px;top:60px;font-size:4.3px;letter-spacing:.5px;color:#bfc3c7;text-transform:uppercase}
.main-nav{position:absolute;left:569px;top:20px;display:flex;gap:10px;font-size:7.2px;font-weight:400;color:var(--white)}
.main-nav span{display:block}
.main-nav .active{color:var(--accent)}
.nav-rule{position:absolute;left:298px;top:52px;width:550px;height:1px;background:var(--rule)}
.nav-active-bar{position:absolute;left:566px;top:51px;width:28px;height:2px;background:var(--accent)}

.hero{position:absolute;left:0;top:73px;width:1053px;height:366px;
  background:
    radial-gradient(ellipse 340px 150px at 560px 120px,rgba(220,226,232,.75),rgba(220,226,232,0) 70%),
    radial-gradient(ellipse 260px 200px at 930px 180px,rgba(30,34,40,.75),rgba(30,34,40,0) 75%),
    radial-gradient(ellipse 240px 180px at 120px 110px,rgba(60,66,74,.6),rgba(60,66,74,0) 75%),
    linear-gradient(180deg,#7e8791 0%,#a6adb5 28%,#6b737c 55%,#3d444b 80%,#2d3339 100%)}
.hero-panel{position:absolute;left:0;top:154px;width:578px;height:184px;background:var(--accent-panel)}
.hero-title{position:absolute;left:246px;top:183px;font-size:17.5px;font-weight:400;color:var(--white);letter-spacing:.2px}
.hero-text{position:absolute;left:247px;top:224px;width:306px;font-size:7px;font-weight:400;line-height:12.1px;color:var(--white)}
.hero-arrow{position:absolute;top:238px}
.hero-dots{position:absolute;left:512px;top:420px;display:flex;gap:4px}
.hero-dots i{display:block;width:7px;height:7px;border:1px solid var(--white);border-radius:50%}
.hero-dots i.on{background:var(--accent);border-color:var(--accent)}

.section-title{position:absolute;left:0;width:915px;top:490px;text-align:center;font-size:16.5px;font-weight:400;letter-spacing:1px;color:var(--text-dark)}
.section-divider{position:absolute;left:455px;top:520px}
.about-copy{position:absolute;left:241px;top:536px;width:270px;font-size:6.9px;line-height:13.2px;font-weight:300;color:var(--text-muted)}
.about-copy p{margin-bottom:13.2px}
.feature{position:absolute;width:272px}
.feature h3{font-size:11.2px;font-weight:400;color:var(--accent);margin-bottom:6px}
.feature p{font-size:6.9px;line-height:13.2px;font-weight:300}
.more{font-size:6.9px;color:var(--accent);line-height:13.2px}
.link-list{list-style:none;margin-left:19px;margin-top:4px}
.link-list li{font-size:6.9px;line-height:13.2px;color:var(--accent);text-decoration:underline}

.estimator{position:absolute;left:543px;top:535px;width:300px;height:200px;
  background:
    radial-gradient(ellipse 150px 110px at 250px 40px,rgba(70,150,190,.55),rgba(70,150,190,0) 75%),
    radial-gradient(ellipse 120px 160px at 110px 60px,rgba(90,96,104,.35),rgba(90,96,104,0) 75%),
    linear-gradient(160deg,#e9edf0 0%,#f6f7f8 45%,#e3e7ea 75%,#ffffff 100%)}
.estimator-label{position:absolute;left:612px;top:608px;width:233px;height:76px;background:var(--accent);color:var(--white);font-size:13px;font-weight:700;text-align:right;padding:9px 14px 0 0;line-height:19.3px}

.commentary{position:absolute;left:543px;top:798px;width:300px;height:302px;
  background:
    radial-gradient(ellipse 110px 70px at 150px 250px,rgba(210,222,228,.7),rgba(210,222,228,0) 75%),
    radial-gradient(ellipse 80px 60px at 40px 280px,rgba(180,200,208,.55),rgba(180,200,208,0) 75%),
    radial-gradient(ellipse 50px 150px at 224px 110px,rgba(120,160,176,.35),rgba(120,160,176,0) 75%),
    linear-gradient(180deg,var(--teal-deep) 0%,var(--teal-mid) 50%,#2f6f86 72%,#7fa3b2 92%,#c6d5db 100%)}
.commentary-line{position:absolute;left:547px;top:969px;width:292px;display:flex;justify-content:space-between;font-size:9.5px;font-weight:600;letter-spacing:1.6px;color:#dfe8ec}

.site-footer{position:absolute;left:0;top:1150px;width:1053px;height:50px;background:var(--footer-bg)}
.footer-links{position:absolute;right:208px;top:15px;text-align:right;font-size:7.2px;line-height:13px;color:var(--accent)}
</style>
</head>
<body>
<header class="site-header">
  <div class="brand"><span class="brand-mark"></span>TRNV LLP</div>
  <div class="brand-sub">Chartered Professional Accountants</div>
  <nav class="main-nav">
    <span class="active">HOME</span><span>ABOUT TRNV</span><span>CERVICES</span><span>LIBRARY</span><span>LINKS</span><span>CAREERS</span><span>CONTACTS</span>
  </nav>
  <div class="nav-rule"></div>
  <div class="nav-active-bar"></div>
</header>

<section class="hero" role="img" aria-label="Silhouettes of business people in a bright office meeting room"></section>
<div class="hero-panel"></div>
<h1 class="hero-title">WELCOME TO TRNV !</h1>
<p class="hero-text">TRNV, Thorne Ravel Nyberg Vance LLP Chartered Accountants, is a full-service, public accounting firm, primarily serving the small and mid-size, entrepreneurial business and professional sectors in Toronto Canada. TRNV's experienced partners and professional, support staff strive to provide accounting and advisory services using an invaluable personal approach, designed to meet each client's individual needs. This "personal touch", combined with a full range of accounting, auditing, tax compliance and planning services allows TRNV to meet all your business and personal accounting requirements.</p>
<svg class="hero-arrow" style="left:14px" width="10" height="16" viewBox="0 0 10 16"><path d="M8 1 L2 8 L8 15" fill="none" stroke="#fff" stroke-width="1.2"/></svg>
<svg class="hero-arrow" style="left:1029px" width="10" height="16" viewBox="0 0 10 16"><path d="M2 1 L8 8 L2 15" fill="none" stroke="#fff" stroke-width="1.2"/></svg>
<div class="hero-dots"><i></i><i class="on"></i><i></i></div>

<h2 class="section-title">ABOUT TRNV</h2>
<svg class="section-divider" width="56" height="10" viewBox="0 0 56 10"><line x1="0" y1="5" x2="23" y2="5" stroke="#555" stroke-width="1"/><circle cx="27" cy="5" r="3.2" fill="#fff" stroke="#555" stroke-width="1"/><line x1="31" y1="5" x2="56" y2="5" stroke="#555" stroke-width="1"/></svg>

<div class="about-copy">
  <p>TRNV, like any good organization is comprised of its people. Its partners. And its staff.</p>
  <p>The founding partners, Robert Thorne, Aki Ravel, Laurie Nyberg and Jim Vance, started TRNV in 1993. Recently, Ron Halvik and Jon Pellow, who have been key members of our TRNV family, joined us as partners. Together we bring over tremendous experience to the practice of public accounting. Experience is not simply a function of getting older. It is the culmination of what life and professional practice have to offer. Hopefully we all learn from this process and are able to apply these lessons and knowledge in whatever we do. We believe at TRNV that we have learned, and that we do apply this experience for the benefit of our clients.</p>
  <p>A more detailed look at our partners and their specific backgrounds and skills can be obtained from the descriptions contained in our Partners Section.</p>
  <p>As important as the partners are, they could not provide the level of service that our clients have come to expect without the dedication of a talented group of professional and support staff. Many senior staff have been with us from the beginning. We expect virtually all of our people will be with us for a long time. We suffer very little staff turnover. That means our staff are happy working at TRNV, we are happy with the contributions that our staff make to the organization, and most importantly our clients can expect a continuity in the people and the service that we provide.</p>
</div>

<div class="feature" style="left:244px;top:848px">
  <h3>Why We Are Different</h3>
  <p>Thorne Ravel Nyberg Vance LLP, affectionately known as TRNV, is a full service public accounting firm primarily serving the small and mid size entrepreneurial business sector in the Greater Toronto Area ("GTA").</p>
  <div class="more">FULL TEXT &gt;&gt;&gt;</div>
</div>

<div class="feature" style="left:242px;top:944px">
  <h3>Staff Profiles</h3>
  <p>We will periodically feature a profile of an existing TRNV staff member, as well as use this area to introduce new members of the firm.</p>
  <div class="more">FULL TEXT &gt;&gt;&gt;</div>
</div>

<div class="feature" style="left:254px;top:1030px;width:130px">
  <h3>Partner Information</h3>
  <ul class="link-list"><li>Robert Thorne</li><li>Aki Ravel</li><li>Laurie Nyberg</li><li>Jim Vance</li></ul>
</div>

<div class="feature" style="left:398px;top:1031px;width:130px">
  <h3>Full Service</h3>
  <ul class="link-list"><li>Accounting and Auditing</li><li>Business Advisory</li><li>Due Diligence</li></ul>
  <div class="more">FULL TEXT &gt;&gt;&gt;</div>
</div>

<div class="estimator" role="img" aria-label="Close-up of a pen resting on a calculator with tax keys over printed figures"></div>
<div class="estimator-label">ONLINE<br>PERSONAL TAX<br>ESTIMATOR 2015</div>

<div class="commentary" role="img" aria-label="Dark teal poster with a sword and misty ground for the personal tax commentary"></div>
<div class="commentary-line"><span>PERSONAL TAX COMMENTARY</span><span>2014-15</span></div>

<footer class="site-footer">
  <div class="footer-links">Site Map | AODA &nbsp;| &nbsp;Privacy Policy<br>© 2006 TRNV Chartered Accountants. All rights reserved.</div>
</footer>
</body>
</html>
```